Application Dashboard Skin - Non coded theme only

We are looking for a website color theme/look feel for a new .net dashboard application we are building. Target audience who will be using this are E and C level professionals. We are looking for the following:

Images of optional color themes for our existing dashboard. You can access a temporary version with no styling here: http://vantorquel.net:99/ . Application built in telerik and highcharts.

We are not looking for finished code or application skins. Our development team will take your final design (with specific colors/images/etc. provided) and apply it to the final beta version of the application.

Design considerations:
We are open to creative ideas, but please know that preference will be given to professional designs with emphasis on a consistent brand look/feel. Designs and colors should be focused on quickly identifying and processing the data.

Multiple submissions welcome.

-Pellowrin team

Target Market(s)

IT / Insurance

Industry/Entity Type

Building

Number of Pages Required

3 page

Requirements
Must have
• Application Dashboard link for design: http://vantorquel.net:99/

```html
<!DOCTYPE html>
<html lang="en">
<head>
<meta charset="utf-8">
<title>Claimview – Accuracy Results</title>
<link rel="stylesheet" href="https://fonts.googleapis.com/css2?family=Noto+Sans:wght@400;600;700&display=swap">
<style>
:root{
  --orange:#f7941d;
  --orange-light:#fdb45c;
  --ink:#3c3c3c;
  --muted:#6b6b6b;
  --slate:#5b6370;
  --band:#5f6670;
  --line:#e3e3e3;
  --stripe:#f1f1f1;
  --page:#eeeeee;
  --white:#ffffff;
}
*{box-sizing:border-box;margin:0;padding:0}
html,body{width:1021px;height:1200px;overflow:hidden}
body{background:var(--page);font-family:"Noto Sans",sans-serif;color:var(--ink);position:relative}
.topbar{position:absolute;left:0;top:0;width:1021px;height:60px;background:var(--white);border-bottom:1px solid #ddd}
.brand{position:absolute;left:25px;top:17px;font-size:19px;font-weight:400;color:#333;display:flex;align-items:center;gap:6px}
.brand-dot{width:12px;height:12px;border-radius:50%;background:var(--orange)}
.nav{position:absolute;top:0;right:0;height:60px;display:flex}
.nav-item{position:absolute;top:0;width:90px;height:60px;text-align:center;font-size:10px;font-weight:600;color:#555}
.nav-item svg{display:block;margin:10px auto 3px}
.nav-item.active::after{content:"";position:absolute;left:12px;right:12px;bottom:0;height:3px;background:var(--orange)}
.nav-sep{position:absolute;top:14px;width:1px;height:32px;background:#ddd}
.panel{position:absolute;background:var(--white);box-shadow:0 1px 2px rgba(0,0,0,.12)}
.panel-head{position:relative;height:48px;border-bottom:1px solid var(--line);display:flex;align-items:center;padding-left:14px;gap:8px}
.panel-title{font-size:13px;font-weight:600;color:#444}
.panel-note{font-size:10px;font-weight:600;color:var(--orange)}
.divider{width:1px;height:14px;background:#ccc;margin:0 6px}
.select{position:absolute;top:12px;height:23px;background:#eaeaea;color:#999;font-size:10px;padding:5px 10px}
.select::after{content:"";position:absolute;right:9px;top:9px;border:5px solid transparent;border-top:6px solid #aaa;border-bottom:0}
.menu{position:absolute;width:14px;height:12px;border-top:2px solid #444;border-bottom:2px solid #444}
.menu::after{content:"";position:absolute;left:0;right:0;top:3px;height:2px;background:#444}
.tabs{position:absolute;left:11px;top:452px;width:705px;height:28px;background:var(--white);display:flex;font-size:10px;font-weight:600;color:#444}
.tab{display:flex;align-items:center;justify-content:center;border-right:1px solid var(--line)}
.tab.active{background:var(--orange);color:var(--white)}
svg text{font-family:"Noto Sans",sans-serif}
.kpi-band{height:30px;background:var(--band);color:var(--white);font-size:10px;font-weight:600;display:flex;align-items:center;justify-content:center}
.kpi-row{height:30.4px;display:flex;align-items:center;font-size:10px;padding-left:12px}
.kpi-row:nth-child(even){background:var(--stripe)}
.kpi-label{width:194px;color:#444}
.kpi-value{font-weight:700;color:#555}
</style>
</head>
<body>

<header class="topbar">
  <div class="brand"><span>Claimview</span><span class="brand-dot"></span></div>
  <nav class="nav">
    <div class="nav-item active" style="left:543px">
      <svg width="20" height="20" viewBox="0 0 20 20"><circle cx="10" cy="10" r="8" fill="none" stroke="var(--orange)" stroke-width="2"/><circle cx="10" cy="10" r="4" fill="none" stroke="var(--orange)" stroke-width="2"/></svg>Accuracy Results</div>
    <div class="nav-sep" style="left:647px"></div>
    <div class="nav-item" style="left:662px">
      <svg width="20" height="20" viewBox="0 0 20 20"><circle cx="10" cy="10" r="8" fill="none" stroke="var(--orange)" stroke-width="2"/><rect x="6" y="6" width="8" height="8" fill="var(--orange)"/></svg>Cessor Accuracy</div>
    <div class="nav-sep" style="left:763px"></div>
    <div class="nav-item" style="left:775px">
      <svg width="20" height="20" viewBox="0 0 20 20"><circle cx="10" cy="10" r="8" fill="none" stroke="var(--orange)" stroke-width="2"/><circle cx="10" cy="8" r="2.5" fill="var(--orange)"/><path d="M5.5 14a4.5 4 0 0 1 9 0z" fill="var(--orange)"/></svg>Manage Users</div>
    <div class="nav-sep" style="left:870px"></div>
    <div class="nav-item" style="left:866px">
      <svg width="20" height="20" viewBox="0 0 20 20"><circle cx="10" cy="10" r="8" fill="none" stroke="var(--orange)" stroke-width="2"/><circle cx="10" cy="10" r="3" fill="none" stroke="var(--orange)" stroke-width="2.5"/></svg>Setting</div>
    <div class="nav-sep" style="left:945px"></div>
    <div class="nav-item" style="left:939px">
      <svg width="20" height="20" viewBox="0 0 20 20"><circle cx="10" cy="10" r="8" fill="none" stroke="var(--orange)" stroke-width="2"/><path d="M7 7.5a4 4 0 1 0 6 0M10 5v5" fill="none" stroke="var(--orange)" stroke-width="1.8"/></svg>Logout</div>
  </nav>
</header>

<!-- YTD accuracy -->
<section class="panel" style="left:11px;top:70px;width:705px;height:317px">
  <div class="panel-head">
    <svg width="18" height="18" viewBox="0 0 18 18"><circle cx="9" cy="9" r="7.5" fill="none" stroke="#555" stroke-width="1.3"/><circle cx="9" cy="9" r="4" fill="none" stroke="#555" stroke-width="1.3"/><circle cx="9" cy="9" r="1.5" fill="#555"/></svg>
    <span class="panel-title">YTD overall accuracy Results</span><span class="divider"></span>
    <span class="panel-note">Click the bars to view YTD details for the specific region</span>
    <div class="select" style="left:531px;width:126px">End to End</div>
    <div class="menu" style="left:675px;top:18px"></div>
  </div>
  <svg width="705" height="269" viewBox="0 48 705 269" style="position:absolute;left:0;top:48px">
    <g stroke="var(--line)" stroke-width="1">
      <line x1="16" y1="66" x2="689" y2="66"/><line x1="16" y1="103" x2="689" y2="103"/><line x1="16" y1="141" x2="689" y2="141"/>
      <line x1="16" y1="178" x2="689" y2="178"/><line x1="16" y1="216" x2="689" y2="216"/><line x1="16" y1="274" x2="689" y2="274"/>
      <line x1="16" y1="48" x2="16" y2="274"/><line x1="47" y1="48" x2="47" y2="274"/><line x1="169" y1="48" x2="169" y2="274"/>
      <line x1="297" y1="48" x2="297" y2="274"/><line x1="426" y1="48" x2="426" y2="274"/><line x1="554" y1="48" x2="554" y2="274"/><line x1="689" y1="48" x2="689" y2="274"/>
    </g>
    <g font-size="10" fill="#555">
      <text x="22" y="69">100</text><text x="22" y="106">97.5</text><text x="22" y="144">95</text>
      <text x="22" y="181">92.5</text><text x="22" y="219">90</text><text x="22" y="257">87.5</text>
    </g>
    <rect x="86" y="108" width="44" height="166" fill="var(--orange)"/>
    <rect x="210" y="98" width="44" height="176" fill="var(--orange-light)"/>
    <rect x="340" y="130" width="44" height="144" fill="var(--orange)"/>
    <rect x="469" y="108" width="44" height="166" fill="var(--orange-light)"/>
    <rect x="598" y="108" width="44" height="166" fill="var(--orange)"/>
    <g font-size="9" font-weight="600" fill="#fff" text-anchor="middle">
      <text x="108" y="124">97.7%</text><text x="232" y="114">98.5%</text><text x="362" y="146">96.8%</text>
      <text x="491" y="124">97.7%</text><text x="620" y="124">94.9%</text>
    </g>
    <g font-size="10" font-weight="600" fill="#444" text-anchor="middle">
      <text x="106" y="299">Colorado</text><text x="232" y="299">Georgia</text><text x="362" y="299">Hawaii</text>
      <text x="494" y="299">Midatlantic</text><text x="621" y="299">Northwest</text>
    </g>
  </svg>
</section>

<!-- Error impact heading -->
<section class="panel" style="left:11px;top:398px;width:705px;height:48px">
  <div class="panel-head" style="border:0">
    <svg width="18" height="16" viewBox="0 0 18 16"><path d="M9 1L17 15H1Z" fill="none" stroke="#555" stroke-width="1.3"/><path d="M9 6v4.5M9 12v1.2" stroke="#555" stroke-width="1.3"/></svg>
    <span class="panel-title" style="font-size:13px">Error impact for june 2016</span>
    <div class="select" style="left:564px;width:126px">All Regions</div>
  </div>
</section>

<nav class="tabs">
  <div class="tab active" style="width:105px">All Errors</div>
  <div class="tab" style="width:104px">Providers</div>
  <div class="tab" style="width:113px">Employers</div>
  <div class="tab" style="width:143px">Line Of Business</div>
</nav>

<!-- Top 10 count -->
<section class="panel" style="left:11px;top:485px;width:705px;height:347px">
  <div class="panel-head" style="height:43px">
    <span class="panel-title">Top 10 Error Reasons</span><span class="divider"></span><span class="panel-note">All Regions</span>
    <div class="menu" style="left:677px;top:16px"></div>
  </div>
  <svg width="705" height="304" viewBox="0 43 705 304" style="position:absolute;left:0;top:43px">
    <g fill="var(--stripe)">
      <rect x="0" y="44" width="190" height="27"/><rect x="0" y="97" width="190" height="27"/><rect x="0" y="151" width="190" height="27"/>
      <rect x="0" y="205" width="190" height="27"/><rect x="0" y="259" width="190" height="27"/>
    </g>
    <g stroke="var(--line)">
      <line x1="190" y1="44" x2="190" y2="313"/><line x1="310" y1="44" x2="310" y2="313"/><line x1="430" y1="44" x2="430" y2="313"/>
      <line x1="551" y1="44" x2="551" y2="313"/><line x1="671" y1="44" x2="671" y2="313"/>
    </g>
    <g font-size="10" fill="#444">
      <text x="11" y="60">Incorrect Contract ...</text><text x="11" y="87">Claim Paid Incorrectly</text>
      <text x="11" y="114">Not A Halvern Benefit.  Bill...</text><text x="11" y="141">Incorrect Co-Pay / C...</text>
      <text x="11" y="167">Copay Amount Not Correct</text><text x="11" y="194">Did Not Follow Desk ...</text>
      <text x="11" y="221">Did Not Follow Pnp</text><text x="11" y="248">Claim Denied In Error...</text>
      <text x="11" y="275">Unknown</text><text x="11" y="302">Denied Incorrectly -...</text>
    </g>
    <g stroke-width="2">
      <line x1="190" y1="57" x2="611" y2="57" stroke="var(--orange)"/><line x1="190" y1="84" x2="513" y2="84" stroke="var(--orange-light)"/>
      <line x1="190" y1="110" x2="483" y2="110" stroke="var(--orange)"/><line x1="190" y1="138" x2="462" y2="138" stroke="var(--orange-light)"/>
      <line x1="190" y1="164" x2="438" y2="164" stroke="var(--orange)"/><line x1="190" y1="191" x2="441" y2="191" stroke="var(--orange-light)"/>
      <line x1="190" y1="218" x2="416" y2="218" stroke="var(--orange)"/><line x1="190" y1="245" x2="368" y2="245" stroke="var(--orange-light)"/>
      <line x1="190" y1="272" x2="368" y2="272" stroke="var(--orange)"/><line x1="190" y1="298" x2="339" y2="298" stroke="var(--orange-light)"/>
    </g>
    <g fill="var(--slate)">
      <circle cx="614" cy="57" r="8"/><circle cx="514" cy="84" r="8"/><circle cx="483" cy="110" r="8"/><circle cx="462" cy="138" r="8"/>
      <circle cx="438" cy="164" r="8"/><circle cx="441" cy="191" r="8"/><circle cx="416" cy="218" r="8"/><circle cx="368" cy="245" r="8"/>
      <circle cx="368" cy="272" r="8"/><circle cx="339" cy="298" r="8"/>
    </g>
    <g font-size="7.5" font-weight="700" fill="#fff" text-anchor="middle">
      <text x="614" y="60">35</text><text x="514" y="87">26</text><text x="483" y="113">24</text><text x="462" y="141">23</text>
      <text x="438" y="167">20</text><text x="441" y="194">20</text><text x="416" y="221">19</text><text x="368" y="248">14</text>
      <text x="368" y="275">14</text><text x="339" y="301">12</text>
    </g>
    <text x="12" y="334" font-size="11" font-weight="600" fill="#444">COUNT</text>
    <g font-size="10" font-weight="600" fill="#555" text-anchor="middle">
      <text x="193" y="333">0</text><text x="311" y="333">10</text><text x="432" y="333">20</text><text x="552" y="333">30</text><text x="668" y="333">40</text>
    </g>
  </svg>
</section>

<!-- Top 10 financial -->
<section class="panel" style="left:11px;top:844px;width:705px;height:346px">
  <div class="panel-head" style="height:42px">
    <span class="panel-title">Top 10 Error Reasons - Financial Impact</span><span class="divider"></span><span class="panel-note">All Regions</span>
    <div class="menu" style="left:677px;top:16px"></div>
  </div>
  <svg width="705" height="304" viewBox="0 42 705 304" style="position:absolute;left:0;top:42px">
    <g fill="var(--stripe)">
      <rect x="0" y="42" width="190" height="27"/><rect x="0" y="96" width="190" height="27"/><rect x="0" y="149" width="190" height="27"/>
      <rect x="0" y="204" width="190" height="27"/><rect x="0" y="259" width="190" height="27"/>
    </g>
    <g stroke="var(--line)">
      <line x1="191" y1="42" x2="191" y2="313"/><line x1="286" y1="42" x2="286" y2="313"/><line x1="382" y1="42" x2="382" y2="313"/>
      <line x1="479" y1="42" x2="479" y2="313"/><line x1="575" y1="42" x2="575" y2="313"/><line x1="671" y1="42" x2="671" y2="313"/>
    </g>
    <g font-size="10" fill="#444">
      <text x="11" y="59">Incorrect Contract ...</text><text x="11" y="86">Claim Paid Incorrectly</text>
      <text x="11" y="112">Not A Halvern Benefit.  Bill...</text><text x="11" y="139">Incorrect Co-Pay / C...</text>
      <text x="11" y="165">Copay Amount Not Correct</text><text x="11" y="193">Did Not Follow Desk ...</text>
      <text x="11" y="221">Did Not Follow Pnp</text><text x="11" y="248">Claim Denied In Error...</text>
      <text x="11" y="276">Unknown</text><text x="11" y="303">Denied Incorrectly -...</text>
    </g>
    <g stroke="var(--orange)" stroke-width="2">
      <line x1="352" y1="55" x2="635" y2="55"/><line x1="446" y1="82" x2="618" y2="82"/><line x1="538" y1="109" x2="575" y2="109"/>
      <line x1="562" y1="136" x2="616" y2="136"/><line x1="532" y1="162" x2="598" y2="162"/><line x1="562" y1="190" x2="598" y2="190"/>
      <line x1="446" y1="218" x2="628" y2="218"/><line x1="562" y1="245" x2="630" y2="245"/><line x1="562" y1="273" x2="612" y2="273"/>
      <line x1="562" y1="300" x2="615" y2="300"/>
    </g>
    <g fill="var(--slate)">
      <rect x="297" y="47" width="58" height="16" rx="8"/><rect x="603" y="47" width="56" height="16" rx="8"/>
      <rect x="403" y="74" width="56" height="16" rx="8"/><rect x="594" y="74" width="50" height="16" rx="8"/>
      <rect x="523" y="101" width="38" height="16" rx="8"/>
      <rect x="542" y="128" width="30" height="16" rx="8"/><rect x="594" y="128" width="50" height="16" rx="8"/>
      <rect x="516" y="154" width="38" height="16" rx="8"/><rect x="586" y="154" width="32" height="16" rx="8"/>
      <rect x="542" y="182" width="30" height="16" rx="8"/><rect x="586" y="182" width="30" height="16" rx="8"/>
      <rect x="403" y="210" width="56" height="16" rx="8"/><rect x="596" y="210" width="56" height="16" rx="8"/>
      <rect x="542" y="237" width="30" height="16" rx="8"/><rect x="602" y="237" width="48" height="16" rx="8"/>
      <rect x="542" y="265" width="30" height="16" rx="8"/><rect x="587" y="265" width="44" height="16" rx="8"/>
      <rect x="542" y="292" width="30" height="16" rx="8"/><rect x="587" y="292" width="52" height="16" rx="8"/>
    </g>
    <g font-size="7.5" font-weight="700" fill="#fff" text-anchor="middle">
      <text x="326" y="58">$ -65155.67</text><text x="631" y="58">$ 12510.63</text>
      <text x="431" y="85">$ -26915.92</text><text x="619" y="85">$ 2919.39</text>
      <text x="542" y="112">$ -245</text>
      <text x="557" y="139">$ 0</text><text x="619" y="139">$ 693.01</text>
      <text x="535" y="165">$ -295</text><text x="602" y="165">$ 10</text>
      <text x="557" y="193">$ 0</text><text x="601" y="193">$ 0</text>
      <text x="431" y="221">$ -29341.33</text><text x="624" y="221">$ 10390.26</text>
      <text x="557" y="248">$ 0</text><text x="626" y="248">$ 6509.7</text>
      <text x="557" y="276">$ 0</text><text x="609" y="276">$ 331.1</text>
      <text x="557" y="303">$ 0</text><text x="613" y="303">$ 1805.56</text>
    </g>
    <text x="12" y="333" font-size="11" font-weight="600" fill="#444">$ Amount</text>
    <g font-size="10" font-weight="600" fill="#555" text-anchor="middle">
      <text x="192" y="333">-80k</text><text x="287" y="333">-60k</text><text x="382" y="333">-40k</text>
      <text x="479" y="333">-20k</text><text x="575" y="333">0k</text><text x="666" y="333">20k</text>
    </g>
  </svg>
</section>

<!-- KPIs -->
<aside class="panel" style="left:726px;top:70px;width:284px;height:480px">
  <div class="panel-head" style="height:46px;border:0;padding-left:12px">
    <svg width="18" height="18" viewBox="0 0 18 18"><circle cx="9" cy="9" r="8" fill="none" stroke="#555" stroke-width="1.3"/><path d="M5 9.5l3 3 5-6" fill="none" stroke="#555" stroke-width="1.5"/></svg>
    <span class="panel-title">KPI's</span>
    <div class="select" style="left:149px;top:11px;width:126px">All Regions</div>
  </div>
  <div class="kpi-band">Overall YTD Accuracy 97.41%</div>
  <div class="kpi-list">
    <div class="kpi-row"><span class="kpi-label">Claims Audited:</span><span class="kpi-value">4859</span></div>
    <div class="kpi-row"><span class="kpi-label">Avg. Claims Audited per day:</span><span class="kpi-value">6.7</span></div>
    <div class="kpi-row"><span class="kpi-label">Errors Found:</span><span class="kpi-value">2147</span></div>
    <div class="kpi-row"><span class="kpi-label">Financial Impact:</span><span class="kpi-value">$1,462,139</span></div>
    <div class="kpi-row"><span class="kpi-label">Total Claims Posted:</span><span class="kpi-value">17,773,591</span></div>
    <div class="kpi-row"><span class="kpi-label">Total Encounter Claims:</span><span class="kpi-value">93,984,586</span></div>
    <div class="kpi-row"><span class="kpi-label">Total Auto Adjudication Claim Count:</span><span class="kpi-value">920,918</span></div>
    <div class="kpi-row"><span class="kpi-label">Total Adjustment Claim Count:</span><span class="kpi-value">920,918</span></div>
    <div class="kpi-row"><span class="kpi-label">Total Denied Claim Count:</span><span class="kpi-value">133,523</span></div>
    <div class="kpi-row"><span class="kpi-label">Total Dollars Paid:</span><span class="kpi-value">$5,669,835,044</span></div>
    <div class="kpi-row"><span class="kpi-label">Auto Adjudication Rate:</span><span class="kpi-value">$0.052</span></div>
    <div class="kpi-row"><span class="kpi-label">Adjustment Rate:</span><span class="kpi-value">1.345%</span></div>
    <div class="kpi-row"><span class="kpi-label">Denial Rate:</span><span class="kpi-value">0.751%</span></div>
  </div>
</aside>

<!-- Paid vs Denied -->
<aside class="panel" style="left:726px;top:550px;width:284px;height:258px;border-top:1px solid var(--line)">
  <div class="menu" style="left:262px;top:23px"></div>
  <svg width="284" height="258" viewBox="0 0 284 258" style="position:absolute;left:0;top:0">
    <circle cx="138" cy="131" r="86" fill="none" stroke="var(--orange)" stroke-width="2.5"/>
    <circle cx="138" cy="131" r="86" fill="none" stroke="var(--slate)" stroke-width="2.5" stroke-dasharray="24 540" transform="rotate(-90 138 131)"/>
    <g text-anchor="middle" font-weight="600">
      <text x="138" y="110" font-size="18" fill="#555">Paid</text>
      <circle cx="138" cy="132" r="10" fill="var(--orange)"/>
      <text x="138" y="136" font-size="10" fill="var(--slate)">vs</text>
      <text x="138" y="164" font-size="18" fill="#555">Denied</text>
      <circle cx="86" cy="62" r="20" fill="var(--orange)"/>
      <text x="86" y="61" font-size="9" fill="#fff">Paid</text><text x="86" y="70" font-size="7" fill="#fff">99.3%</text>
      <circle cx="190" cy="202" r="20" fill="var(--slate)"/>
      <text x="190" y="201" font-size="8.5" fill="#fff">Denied</text><text x="190" y="210" font-size="7" fill="#fff">0.7%</text>
    </g>
  </svg>
</aside>

<!-- Paid vs Encounter -->
<aside class="panel" style="left:726px;top:808px;width:284px;height:284px;border-top:1px solid var(--line)">
  <div class="menu" style="left:262px;top:24px"></div>
  <svg width="284" height="284" viewBox="0 0 284 284" style="position:absolute;left:0;top:0">
    <circle cx="138" cy="139" r="86" fill="none" stroke="var(--orange)" stroke-width="2.5"/>
    <circle cx="138" cy="139" r="86" fill="none" stroke="var(--slate)" stroke-width="2.5" stroke-dasharray="150 540" transform="rotate(168 138 139)"/>
    <g text-anchor="middle" font-weight="600">
      <text x="138" y="118" font-size="18" fill="#555">Paid</text>
      <circle cx="138" cy="140" r="10" fill="var(--orange)"/>
      <text x="138" y="144" font-size="10" fill="var(--slate)">vs</text>
      <text x="138" y="172" font-size="18" fill="#555">Encounter</text>
      <circle cx="86" cy="70" r="20" fill="var(--slate)"/>
      <text x="86" y="69" font-size="9" fill="#fff">Paid</text><text x="86" y="78" font-size="7" fill="#fff">15.9%</text>
      <circle cx="190" cy="210" r="20" fill="var(--orange)"/>
      <text x="190" y="209" font-size="8.5" fill="#fff">Denied</text><text x="190" y="218" font-size="7" fill="#fff">84.1%</text>
    </g>
  </svg>
</aside>

</body>
</html>
```